Introducing a Personal Care Product called" VELO"

We are a nutra-pharmaceutical company launching a new personal care product called VELO. Some of the products include massage and aroma therapy, as well as personal lubricants. The products will be produced and put into, two bottles that are interlocking so two combinations of products can be purchased at once (i.e. massage and aroma therapy). The poster will be used for promotional advertising, trade shows and for in-store promotions.
Updates

We would like to see a design without the product.

Target Market(s)

Products will be aimed at adults primarily women 18-65 in the USA. We want to appeal to the everyday woman who is interested in their sexual well being.

Industry/Entity Type

Massage

Requirements
Must have
• Clean Presentation. Not many colors. Text should be as follows: VELO for Her....VELO for Him...VELO for You...Let's VELO see attached..Also VELO with Her...Velo with Him..Let's VELO..Open to other copy versions.
Nice to have
• Product image not necessary but can be used. image attached
Should not have
• Too many colors...

```html
<!DOCTYPE html>
<html lang="en">
<head>
<meta charset="utf-8">
<title>ovela — with her, with him</title>
<link rel="stylesheet" href="https://fonts.googleapis.com/css2?family=Jost:wght@400&family=Great+Vibes&display=swap">
<style>
  :root {
    --pink: #f995dc;
    --aqua: #9ef7f5;
    --paper: #ffffff;
    --ink: #111111;
    --grey: #7b8283;
    --her: #d0406e;
    --him: #1d3a8f;
    --shade: rgba(0, 0, 0, 0.55);
  }
  html, body {
    margin: 0;
    padding: 0;
    width: 862px;
    height: 1200px;
    overflow: hidden;
    background: var(--paper);
  }
  .poster {
    position: relative;
    width: 862px;
    height: 1200px;
    overflow: hidden;
    background: var(--paper);
    font-family: "Jost", "Futura", sans-serif;
    color: var(--ink);
  }
  .backdrop {
    position: absolute;
    inset: 0;
  }
  .band-her { fill: var(--pink); filter: drop-shadow(0 6px 4px var(--shade)); }
  .band-him { fill: var(--aqua); filter: drop-shadow(0 -6px 4px var(--shade)); }
  .symbol { fill: none; stroke: var(--paper); filter: drop-shadow(4px 5px 3px rgba(0,0,0,0.45)); }
  .symbol-solid { fill: var(--paper); filter: drop-shadow(4px 5px 3px rgba(0,0,0,0.45)); }

  .line {
    position: absolute;
    margin: 0;
    line-height: 1;
    white-space: nowrap;
  }
  .word-brand { font-size: 118px; font-weight: 400; letter-spacing: -2px; }
  .word-with { font-size: 72px; font-weight: 400; }
  .word-script {
    font-family: "Great Vibes", cursive;
    font-size: 300px;
  }
  .her { color: var(--her); }
  .him { color: var(--him); }

  .headline-her .word-brand { left: 38px; top: 62px; }
  .headline-her .word-with { left: 92px; top: 203px; }
  .headline-her .word-script { left: 215px; top: 160px; }

  .tagline {
    left: 86px;
    top: 520px;
    font-size: 92px;
  }
  .tagline .lead { color: var(--grey); }

  .headline-him .word-brand { left: 290px; top: 858px; }
  .headline-him .word-with { left: 338px; top: 985px; }
  .headline-him .word-script { left: 478px; top: 925px; }

  .product-shot {
    position: absolute;
    left: 538px;
    top: 418px;
    width: 266px;
    height: 290px;
    border-radius: 14px;
    background: linear-gradient(90deg, #f3c3d4 0%, #eef0f2 50%, #bfe6f3 100%);
  }
</style>
</head>
<body>
<main class="poster">
  <svg class="backdrop" width="862" height="1200" viewBox="0 0 862 1200" aria-hidden="true">
    <path class="band-her" d="M0 0 H862 V282 C700 290 560 330 470 400 C380 470 250 560 0 552 Z"/>
    <path class="band-him" d="M0 702 C120 660 230 630 330 640 C470 655 560 760 700 810 C760 830 820 838 862 838 V1200 H0 Z"/>

    <g class="venus">
      <circle class="symbol" cx="612" cy="-24" r="120" stroke-width="24"/>
      <rect class="symbol-solid" x="598" y="98" width="28" height="198"/>
      <rect class="symbol-solid" x="522" y="188" width="168" height="32"/>
    </g>

    <g class="mars">
      <circle class="symbol" cx="108" cy="1010" r="175" stroke-width="26"/>
      <path class="symbol" d="M232 870 L318 738" stroke-width="28"/>
      <path class="symbol-solid" d="M205 700 H340 V832 H312 V728 H205 Z"/>
    </g>
  </svg>

  <section class="headline-her">
    <p class="line word-brand">ovela</p>
    <p class="line word-with">with</p>
    <p class="line word-script her">her</p>
  </section>

  <p class="line tagline"><span class="lead">...lets</span> ovela</p>

  <div class="product-shot" role="img" aria-label="Photo of two interlocking ovela lubricant bottles, a pink 'her' bottle and a blue 'him' bottle, with reflection"></div>

  <section class="headline-him">
    <p class="line word-brand">ovela</p>
    <p class="line word-with">with</p>
    <p class="line word-script him">him</p>
  </section>
</main>
</body>
</html>
```